STI/STD Medical Clinic- Wellpoint Cedar Partners, Inc Website

We are a STI clinic in florida looking for a website. We want to be professional but also playful. We want a buildout similar to the website listed below as our clinic is very similar to theirs.

This is a great example of a clinic doing similar stuff as us. We obviously do not want their color scheme but their format and buildout work. Please see our logo attached for color schemes etc.

https://brightfieldcaretampa.org

Industry/Entity Type

Medical

Coding

Coded - Design and coding required

Number of Pages Required

5+ page

Font styles to use
Sans Serif

```html
<!DOCTYPE html>
<html lang="en">
<head>
<meta charset="utf-8">
<title>Wellpoint Cedar Partners, Inc</title>
<link href="https://fonts.googleapis.com/css2?family=Poppins:wght@400;500;600;700&display=swap" rel="stylesheet">
<style>
:root{
  --blue:#1f7bf2;
  --blue-deep:#2d4fe3;
  --violet:#7b3ff0;
  --pink:#e040c8;
  --coral:#ff5a6e;
  --orange:#ff7a3d;
  --ink:#1d1d28;
  --muted:#55576a;
  --light:#f5f6fb;
  --footer:#2e2f38;
  --footer-dark:#25262d;
  --white:#ffffff;
}
*{box-sizing:border-box;margin:0;padding:0}
html,body{width:1200px;height:4827px;overflow:hidden}
body{font-family:'Poppins',sans-serif;color:var(--ink);background:var(--white);position:relative}
.abs{position:absolute}
section,header,footer{position:absolute;left:0;width:1200px}

/* header */
.site-header{top:0;height:114px;background:var(--white)}
.top-bar{position:absolute;left:384px;top:0;width:816px;height:41px;background:linear-gradient(90deg,var(--blue),var(--blue-deep));border-bottom-left-radius:40px;display:flex;align-items:center;padding-left:234px;gap:30px;color:var(--white);font-size:16px}
.top-bar span.sep{opacity:.8}
.brand{position:absolute;left:103px;top:30px;display:flex;align-items:center;gap:12px}
.brand-dot{width:46px;height:46px;border-radius:50%;background:var(--coral)}
.brand-name{font-weight:700;font-size:22px;line-height:1.05;color:var(--blue-deep);width:200px}
.main-nav{position:absolute;left:409px;top:67px;display:flex;gap:45px;font-size:16px;font-weight:500}
.main-nav a{color:var(--ink);text-decoration:none}
.main-nav a.active{color:var(--coral)}

/* hero */
.hero{top:114px;height:655px}
.hero-photo{position:absolute;inset:0;background:linear-gradient(180deg,#3d3a7a 0%,#7a5aa0 30%,#c06a8a 50%,#2c3a6e 75%,#1a2350 100%)}
.hero h1{position:absolute;left:98px;top:192px;color:var(--white);font-size:66px;font-weight:600;line-height:1;letter-spacing:1px}
.hero p{position:absolute;left:100px;top:330px;width:440px;color:var(--white);font-size:16px;line-height:26px}
.btn{display:inline-flex;align-items:center;justify-content:center;font-weight:500;font-size:15px;border-radius:6px;text-decoration:none}
.hero .btn{position:absolute;top:405px;height:44px;color:var(--white)}
.btn-book{left:101px;width:208px;background:var(--blue)}
.btn-services{left:319px;width:210px;background:linear-gradient(90deg,var(--violet),var(--pink))}

/* feature cards */
.feature-card{position:absolute;top:731px;width:314px;height:388px;border-radius:20px;color:var(--white);text-align:center}
.feature-card.prep{left:99px;background:linear-gradient(160deg,#1a8cff,#2b50e8)}
.feature-card.hepc{left:443px;background:linear-gradient(160deg,#7b3ff0,#e040c8)}
.feature-card.hiv{left:788px;background:linear-gradient(160deg,#ff4d8a,#ff6a3d)}
.feature-icon{position:absolute;left:108px;top:38px;width:97px;height:97px;border-radius:50%;background:var(--white);display:flex;align-items:center;justify-content:center}
.feature-card h3{position:absolute;top:150px;width:100%;font-size:25px;font-weight:500}
.feature-card p{position:absolute;top:196px;left:30px;width:254px;font-size:13px;line-height:31px}
.feature-card .btn{position:absolute;top:308px;left:72px;width:169px;height:43px;background:var(--white);color:var(--ink);font-size:15px}

/* clinic */
.clinic{top:1213px;height:643px;background:var(--light)}
.clinic-dots{position:absolute;left:70px;top:305px;width:280px;height:300px;background-image:radial-gradient(circle,#f2a0b0 1.6px,transparent 2px);background-size:14px 14px;opacity:.8}
.clinic-photo{position:absolute;left:103px;top:77px;width:473px;height:454px;border-radius:90px 0 0 0;background:linear-gradient(135deg,#f0ebe6,#d9d2cb 60%,#b8ac9e)}
.clinic h2{position:absolute;left:645px;top:140px;font-size:36px;font-weight:600}
.clinic p{position:absolute;left:647px;top:205px;width:450px;font-size:13px;line-height:31px;color:var(--muted)}
.clinic .btn{position:absolute;left:647px;top:452px;width:148px;height:45px;background:var(--blue);color:var(--white)}

/* services */
.services{top:1856px;height:876px;background:linear-gradient(135deg,#1e90ff 0%,#2f6ff0 55%,#3a4fe0 100%);color:var(--white);text-align:center}
.services h2{position:absolute;top:70px;width:100%;font-size:40px;font-weight:600}
.services .intro{position:absolute;top:138px;left:180px;width:840px;font-size:14px;line-height:30px}
.service{position:absolute;width:250px;text-align:center}
.service .icon{width:112px;height:112px;margin:0 auto;border-radius:50%;background:var(--white);box-shadow:0 0 0 8px rgba(255,255,255,.25);display:flex;align-items:center;justify-content:center}
.service h3{font-size:18px;font-weight:500;line-height:22px;margin-top:18px}
.service p{font-size:12px;line-height:26px;margin:6px auto 0;width:230px}
.service.highlight{background:var(--white);color:var(--ink);padding-top:22px;height:287px;width:251px;border-radius:6px}
.service.highlight .icon{background:linear-gradient(135deg,#ff6f7e,#f23a5a);box-shadow:0 0 0 8px #ffe1e6}

/* team */
.team{top:2732px;height:746px;background:var(--white)}
.team h2{position:absolute;top:84px;width:100%;text-align:center;font-size:40px;font-weight:600}
.team-photo{position:absolute;top:167px;width:475px;height:399px;border-radius:22px}
.team-photo.one{left:111px;background:linear-gradient(135deg,#e9e3de,#cdbfb6 60%,#b89a84)}
.team-photo.two{left:613px;background:linear-gradient(135deg,#2f5a6a,#1f3f52 60%,#3b6c7a)}
.arrow{position:absolute}
.team .btn{position:absolute;left:525px;top:607px;width:150px;height:42px;background:var(--blue);color:var(--white)}

/* partners */
.partners{top:3478px;height:343px;background:#f7f7f9}
.partners h2{position:absolute;top:60px;width:100%;text-align:center;font-size:40px;font-weight:600}
.partner{position:absolute;top:159px;width:232px;height:109px;background:var(--white);box-shadow:0 4px 14px rgba(0,0,0,.06);display:flex;align-items:center;justify-content:center;gap:10px;font-weight:700;font-size:26px}
.partner .mark{width:30px;height:30px;border-radius:50%;background:var(--coral)}

/* booking */
.booking{top:3821px;height:657px;background:linear-gradient(180deg,#5a3fe2 0%,#8a44e2 60%,#ad46de 100%);color:var(--white)}
.booking h2{position:absolute;top:72px;width:100%;text-align:center;font-size:37px;font-weight:500;line-height:46px}
.booking .lead{position:absolute;top:184px;width:100%;text-align:center;font-size:18px}
.field{position:absolute;background:var(--white);color:#555;font-size:15px;padding:12px 20px;border-radius:2px}
.label{position:absolute;left:209px;font-size:15px;font-weight:600}
.radios{position:absolute;left:218px;top:572px;display:flex;gap:12px;font-size:15px}
.radios span{display:flex;align-items:center;gap:6px}
.radios i{width:14px;height:14px;border:1.5px solid var(--white);border-radius:50%;display:inline-block}
.booking .btn{position:absolute;left:821px;top:527px;width:167px;height:43px;background:var(--white);color:var(--ink);border-radius:3px}

/* footer */
.site-footer{top:4478px;height:349px;background:var(--footer);color:#d8d8e0}
.footer-brand{position:absolute;left:103px;top:78px;display:flex;align-items:center;gap:14px}
.footer-brand .brand-dot{width:60px;height:60px}
.footer-brand .brand-name{color:var(--white);font-size:26px;width:240px}
.social{position:absolute;left:146px;top:200px;display:flex;gap:10px}
.social span{width:34px;height:34px;border-radius:50%;background:#ff3b55;display:block}
.footer-col{position:absolute;top:70px}
.footer-col h4{font-size:15px;font-weight:600;color:var(--white);letter-spacing:.5px;margin-bottom:14px}
.footer-col li{list-style:none;font-size:13px;line-height:26px}
.divider{position:absolute;top:110px;width:0;height:180px;border-left:1px dashed #777}
.contact-row{display:flex;align-items:center;gap:14px;font-size:13px;line-height:20px;margin-bottom:14px}
.contact-row .ic{width:34px;height:34px;border:1.5px solid #ccc;border-radius:50%;display:flex;align-items:center;justify-content:center;flex:none}
.copyright{position:absolute;left:0;bottom:0;width:100%;height:55px;background:var(--footer-dark);text-align:center;line-height:55px;font-size:13px}
</style>
</head>
<body>

<header class="site-header">
  <div class="top-bar"><span>Patient Portal</span><span class="sep">|</span><span>Patient Messaging App</span><span class="sep">|</span><span>Donate</span></div>
  <div class="brand"><span class="brand-dot"></span><span class="brand-name">Wellpoint Cedar Partners</span></div>
  <nav class="main-nav">
    <a class="active" href="#">Home</a><a href="#">About</a><a href="#">Meet The Team</a><a href="#">Services</a><a href="#">News</a><a href="#">FAQs</a><a href="#">Contact</a>
  </nav>
</header>

<section class="hero">
  <div class="hero-photo" role="img" aria-label="City skyline at dusk with a lit bridge reflected on the river"></div>
  <h1>WELLPOINT<br>CEDAR PARTNERS</h1>
  <p>At vero eos et accusamus etsto odio dignissimos ducimus qui blanditiis praesentium</p>
  <a class="btn btn-book" href="#">Book an Appointment</a>
  <a class="btn btn-services" href="#">Get a Services</a>
</section>

<div class="feature-card prep">
  <div class="feature-icon"><svg width="50" height="50" viewBox="0 0 50 50"><rect x="8" y="17" width="34" height="16" rx="8" fill="none" stroke="#1f7bf2" stroke-width="3" transform="rotate(-35 25 25)"/><line x1="25" y1="14" x2="25" y2="36" stroke="#1f7bf2" stroke-width="3" transform="rotate(-35 25 25)"/></svg></div>
  <h3>PrEP</h3>
  <p>Sed ut perspiciatis unde nis iste natus error sit voluptatem accusantium doloremque laudantium,</p>
  <a class="btn" href="#">Learn More</a>
</div>
<div class="feature-card hepc">
  <div class="feature-icon"><svg width="50" height="50" viewBox="0 0 50 50"><path d="M6 22c0-6 6-9 14-8 8 1 14-2 20-2 4 0 5 4 3 8-3 7-11 16-20 18-9 2-17-6-17-16z" fill="none" stroke="#8a3fe8" stroke-width="3"/><circle cx="36" cy="12" r="7" fill="#fff" stroke="#8a3fe8" stroke-width="2.5"/><path d="M36 8v8M32 12h8" stroke="#8a3fe8" stroke-width="2.5"/></svg></div>
  <h3>Hepatitis C</h3>
  <p>Sed ut perspiciatis unde nis iste natus error sit voluptatem accusantium doloremque laudantium,</p>
  <a class="btn" href="#">Learn More</a>
</div>
<div class="feature-card hiv">
  <div class="feature-icon"><svg width="50" height="50" viewBox="0 0 50 50"><path d="M25 28 L14 44 M25 28 L36 44 M25 28 C17 18 17 6 25 6 C33 6 33 18 25 28" fill="none" stroke="#ff4d6a" stroke-width="3.5" stroke-linecap="round"/></svg></div>
  <h3>HIV</h3>
  <p>Sed ut perspiciatis unde nis iste natus error sit voluptatem accusantium doloremque laudantium,</p>
  <a class="btn" href="#">Learn More</a>
</div>

<section class="clinic">
  <div class="clinic-dots"></div>
  <div class="clinic-photo" role="img" aria-label="Bright clinic waiting room with a sofa and the clinic name on the wall"></div>
  <h2>MEET OUR CLINIC</h2>
  <p>At vero eos et accusamus et iusto odio digcus qui blanditiis praesentium voluptatum deleniti atquerrupti quos dolores et quas molestias excepturi sint occaecati cupiditate non provident, similique sunt in culpa qui officia deserunt mollitia animi, id est laborum et dolorum fuga. Et harum quidem rerum facilis est et expedita octio. Nam libero tempore, cum soluta nobis est eligendi optio cumque nihil imped qo minus id quod maxime placeat facere possimus, omnis voluptas assumenda</p>
  <a class="btn" href="#">Learn More</a>
</section>

<section class="services">
  <h2>OUR SERVICES</h2>
  <p class="intro">At vero eos et accusamus et iusto odio dignissimos ducimus qui blanditiis praesenti voluptatum deleniti atque corrupti quos dolores et qmolestias excepturi sint occaecati cupiditate non provint, similique sunt in culpa</p>

  <div class="service" style="left:83px;top:244px">
    <div class="icon"><svg width="52" height="52" viewBox="0 0 52 52" fill="none" stroke="#2d5fe8" stroke-width="2.5"><path d="M12 6v14a8 8 0 0016 0V6M20 28v8a10 10 0 0020 0v-6"/><circle cx="40" cy="26" r="4"/></svg></div>
    <h3>PrEP</h3><p>Sed ut perspiciatis unde nis iste natus er sit voluptaccusantium doloremque laudantium,</p>
  </div>
  <div class="service" style="left:344px;top:244px">
    <div class="icon"><svg width="52" height="52" viewBox="0 0 52 52" fill="none" stroke="#2d5fe8" stroke-width="2.5"><rect x="10" y="8" width="16" height="30" rx="8" transform="rotate(-30 18 23)"/><ellipse cx="34" cy="36" rx="12" ry="7"/><line x1="22" y1="36" x2="46" y2="36"/></svg></div>
    <h3>PeP</h3><p>Sed ut perspiciatis unde nis iste natus er sit voluptaccusantium doloremque laudantium,</p>
  </div>
  <div class="service highlight" style="left:608px;top:220px">
    <div class="icon"><svg width="52" height="52" viewBox="0 0 50 50"><path d="M6 22c0-6 6-9 14-8 8 1 14-2 20-2 4 0 5 4 3 8-3 7-11 16-20 18-9 2-17-6-17-16z" fill="none" stroke="#fff" stroke-width="3"/><circle cx="36" cy="12" r="7" fill="none" stroke="#fff" stroke-width="2.5"/><path d="M36 8v8M32 12h8" stroke="#fff" stroke-width="2.5"/></svg></div>
    <h3>Hepatitis C</h3><p>Sed ut perspiciatis unde nis iste natus er sit voluptaccusantium doloremque laudantium,</p>
  </div>
  <div class="service" style="left:867px;top:244px">
    <div class="icon"><svg width="52" height="52" viewBox="0 0 50 50"><path d="M25 28 L14 44 M25 28 L36 44 M25 28 C17 18 17 6 25 6 C33 6 33 18 25 28" fill="none" stroke="#2d5fe8" stroke-width="3" stroke-linecap="round"/></svg></div>
    <h3>HIV</h3><p>Sed ut perspiciatis unde nis iste natus er sit voluptaccusantium doloremque laudantium,</p>
  </div>

  <div class="service" style="left:83px;top:542px">
    <div class="icon"><svg width="52" height="52" viewBox="0 0 52 52" fill="none" stroke="#2d5fe8" stroke-width="2.5"><circle cx="26" cy="26" r="11"/><path d="M26 6v9M26 37v9M6 26h9M37 26h9M12 12l6 6M34 34l6 6M40 12l-6 6M18 34l-6 6"/></svg></div>
    <h3>STI</h3><p>Sed ut perspiciatis unde nis iste natus er sit voluptaccusantium doloremque laudantium,</p>
  </div>
  <div class="service" style="left:344px;top:542px">
    <div class="icon"><svg width="52" height="52" viewBox="0 0 52 52" fill="none" stroke="#2d5fe8" stroke-width="2.5"><rect x="12" y="8" width="28" height="38" rx="3"/><path d="M20 6h12v6H20zM18 22h16M18 30h16M18 38h10"/></svg></div>
    <h3>Case Management<br>(Non-Medical)</h3><p>Sed ut perspiciatis unde nis iste natus er sit voluptaccusantium</p>
  </div>
  <div class="service" style="left:606px;top:542px">
    <div class="icon"><svg width="52" height="52" viewBox="0 0 52 52" fill="none" stroke="#2d5fe8" stroke-width="2.5"><rect x="8" y="8" width="36" height="26" rx="2"/><path d="M20 42h12M26 34v8"/><circle cx="26" cy="18" r="5"/><path d="M17 30c2-5 16-5 18 0"/></svg></div>
    <h3>Telehealth<br>(Telemedicine)</h3><p>Sed ut perspiciatis unde nis iste natus er sit voluptaccusantium</p>
  </div>
  <div class="service" style="left:867px;top:542px">
    <div class="icon"><svg width="52" height="52" viewBox="0 0 52 52" fill="none" stroke="#2d5fe8" stroke-width="2.5"><ellipse cx="22" cy="28" rx="15" ry="11"/><path d="M12 37l-4 7 9-4"/><ellipse cx="34" cy="16" rx="11" ry="8"/></svg></div>
    <h3>Language Interpretation<br>Services</h3><p>Sed ut perspiciatis unde nis iste natus er sit voluptaccusantium</p>
  </div>
</section>

<section class="team">
  <h2>MEET THE TEAM</h2>
  <div class="team-photo one" role="img" aria-label="Three smiling staff members seated together on a sofa"></div>
  <div class="team-photo two" role="img" aria-label="Five team members standing in a row against a teal wall"></div>
  <svg class="arrow" style="left:66px;top:350px" width="20" height="40" viewBox="0 0 20 40"><path d="M18 2L2 20l16 18" fill="none" stroke="#444" stroke-width="2"/></svg>
  <svg class="arrow" style="left:1110px;top:350px" width="20" height="40" viewBox="0 0 20 40"><path d="M2 2l16 18L2 38" fill="none" stroke="#444" stroke-width="2"/></svg>
  <a class="btn" href="#">Our Team</a>
</section>

<section class="partners">
  <h2>OUR PARTNERS</h2>
  <svg class="arrow" style="left:70px;top:202px" width="14" height="26" viewBox="0 0 14 26"><path d="M12 1L2 13l10 12" fill="none" stroke="#444" stroke-width="2"/></svg>
  <div class="partner" style="left:99px"><span class="mark"></span>Medvale</div>
  <div class="partner" style="left:354px"><span class="mark"></span>Orbitline</div>
  <div class="partner" style="left:609px"><span class="mark"></span>Kestrel</div>
  <div class="partner" style="left:864px"><span class="mark"></span>Quadra</div>
  <svg class="arrow" style="left:1113px;top:202px" width="14" height="26" viewBox="0 0 14 26"><path d="M2 1l10 12L2 25" fill="none" stroke="#444" stroke-width="2"/></svg>
</section>

<section class="booking">
  <h2>Now Booking For TeleHealth &amp;<br>In-Person Appointments</h2>
  <p class="lead">Fill out the form to make an appointment</p>
  <div class="field" style="left:204px;top:238px;width:387px;height:47px">Your name</div>
  <div class="field" style="left:602px;top:238px;width:388px;height:47px">Phone</div>
  <div class="field" style="left:204px;top:300px;width:786px;height:47px">Your e-mail</div>
  <div class="label" style="top:371px">What are you inquiring about?</div>
  <div class="field" style="left:204px;top:405px;width:786px;height:94px">Additional Info</div>
  <div class="label" style="top:525px">What is your appointment preference?</div>
  <div class="radios"><span><i></i>In-Person</span><span><i></i>Telehealth</span></div>
  <a class="btn" href="#">Submit</a>
</section>

<footer class="site-footer">
  <div class="footer-brand"><span class="brand-dot"></span><span class="brand-name">Wellpoint Cedar Partners</span></div>
  <div class="social" aria-label="Social media links"><span></span><span></span><span></span><span></span><span></span></div>

  <div class="footer-col" style="left:471px">
    <h4>QUICK LINKS</h4>
    <ul><li>Home</li><li>About</li><li>Meet The Team</li><li>Services</li><li>News</li><li>FAQs</li><li>Contact</li></ul>
  </div>
  <div class="divider" style="left:613px"></div>
  <div class="footer-col" style="left:658px">
    <h4>USEFUL LINKS</h4>
    <ul><li>&gt; Lorem Ipsum passage</li><li>&gt; Sed ut perspiciatis</li><li style="margin-top:10px">&gt; At vero eos et accusa</li><li style="margin-top:8px">&gt; Dolor sit ame</li></ul>
  </div>
  <div class="divider" style="left:857px"></div>
  <div class="footer-col" style="left:894px">
    <h4>CONTACT DETAILS</h4>
    <div class="contact-row"><span class="ic"><svg width="14" height="18" viewBox="0 0 14 18"><path d="M7 17s6-6 6-10A6 6 0 001 7c0 4 6 10 6 10z" fill="none" stroke="#ddd" stroke-width="1.6"/><circle cx="7" cy="7" r="2" fill="#ddd"/></svg></span><span>4410 Palmetto Way<br>Tampa FL 33602</span></div>
    <div class="contact-row"><span class="ic"><svg width="16" height="16" viewBox="0 0 16 16"><path d="M3 1l3 3-2 2c1 2 4 5 6 6l2-2 3 3-2 2C7 15 1 9 1 3z" fill="none" stroke="#ddd" stroke-width="1.4"/></svg></span><span>+1 813 555 0142</span></div>
    <div class="contact-row"><span class="ic"><svg width="16" height="12" viewBox="0 0 16 12"><rect x="1" y="1" width="14" height="10" fill="none" stroke="#ddd" stroke-width="1.4"/><path d="M1 1l7 6 7-6" fill="none" stroke="#ddd" stroke-width="1.4"/></svg></span><span>info@wcpclinic.org</span></div>
  </div>
  <div class="copyright">©Copyright ©2022 WCP. All Rights Reserved.</div>
</footer>

</body>
</html>
```